Pre-Paid Card for Teens needs a design

We are a Fintech company called Zorvella. We will sell prepaid cards for families and teens. Now we need a prepaid card design. Prepaid card should have a plexicard logo, company logo, 16 card number, expire date. Our webpage is http://www.zorvella-example.com
Target Market(s)
Teenages between 8 - 18 years old
Industry/Entity Type
It Company
Requirements
Must have
- The prepaid card must include zorvella logo, plexicard debit card logo (I already attached a sample card), 16 digit card number and expire date.
Nice to have
- It should be fun and prestigious for young people.
Should not have
- We don't want that the card has a lots of color

```html
<!DOCTYPE html>
<html lang="en">
<head>
<meta charset="utf-8">
<title>Zorvella Prepaid Card</title>
<link rel="stylesheet" href="https://fonts.googleapis.com/css2?family=Work+Sans:wght@300;400;600&display=swap">
<style>
  :root {
    --page-bg: #ffffff;
    --card-purple: #55198f;
    --card-purple-light: #6a2ca3;
    --card-purple-dark: #431270;
    --number-yellow: #e6dc3c;
    --brand-yellow: #fdf542;
    --lilac: #c27ae8;
    --lilac-bright: #d779fb;
  }
  * { box-sizing: border-box; margin: 0; padding: 0; }
  html, body {
    width: 1200px;
    height: 1066px;
    overflow: hidden;
    background: var(--page-bg);
    font-family: "Work Sans", Arial, sans-serif;
  }
  .canvas {
    position: relative;
    width: 1200px;
    height: 1066px;
  }
  .prepaid-card {
    position: absolute;
    left: 100px;
    top: 218px;
    width: 1000px;
    height: 630px;
    border-radius: 44px;
    background: linear-gradient(125deg, var(--card-purple) 0%, var(--card-purple-light) 45%, var(--card-purple-dark) 46%, var(--card-purple) 100%);
    overflow: hidden;
  }
  .brand {
    position: absolute;
    left: 70px;
    top: 200px;
    display: flex;
    align-items: center;
    gap: 18px;
  }
  .brand-dot {
    width: 64px;
    height: 64px;
    border-radius: 50%;
    background: var(--lilac-bright);
  }
  .brand-name {
    font-weight: 600;
    font-size: 58px;
    color: var(--brand-yellow);
    letter-spacing: 0.01em;
  }
  .card-details {
    position: absolute;
    left: 400px;
    top: 318px;
    display: flex;
    flex-direction: column;
  }
  .card-number {
    font-weight: 400;
    font-size: 40px;
    line-height: 1.1;
    letter-spacing: 0.04em;
    word-spacing: 0.6em;
    color: var(--number-yellow);
    white-space: nowrap;
  }
  .holder-name {
    margin-top: 14px;
    font-weight: 300;
    font-size: 24px;
    letter-spacing: 0.06em;
    color: var(--lilac);
    text-transform: uppercase;
    white-space: nowrap;
  }
  .expiry {
    margin-top: 18px;
    align-self: flex-end;
    font-weight: 300;
    font-size: 24px;
    letter-spacing: 0.08em;
    color: var(--lilac);
  }
  .network {
    position: absolute;
    right: 70px;
    bottom: 52px;
    display: flex;
    align-items: center;
    gap: 10px;
  }
  .network-dot {
    width: 34px;
    height: 34px;
    border-radius: 50%;
    background: var(--lilac);
  }
  .network-name {
    font-weight: 600;
    font-size: 28px;
    color: var(--brand-yellow);
  }
</style>
</head>
<body>
  <main class="canvas">
    <section class="prepaid-card" aria-label="Zorvella prepaid card">
      <div class="brand">
        <span class="brand-dot"></span>
        <span class="brand-name">Zorvella</span>
      </div>
      <div class="card-details">
        <p class="card-number">5328 2178 9012 3456</p>
        <p class="holder-name">Lena Marsh</p>
        <p class="expiry">07/24</p>
      </div>
      <div class="network">
        <span class="network-dot"></span>
        <span class="network-name">plexicard</span>
      </div>
    </section>
  </main>
</body>
</html>
```